Pharma compliance business needs an eye catching academic poster

Academic poster for display at a pharma industry conference

Background

CodaVetta Ltd is an online, on-demand supplier of compliance advice (copy review) to the life science industry. See www.codavetta.co.uk for more info.

We have conducted a benchmarking study on the time spent by three large pharma companies on copy review. It highlights time spent and time wasted as a result of unnecessary, additional rounds of review. As a result we have developed recommendation for improving the copy review process.

Requirement

We need an academic poster A0 Landscape (841 x 1189 mm) that summaries our methodology, results and conclusions. We have written the copy - see attached.

This poster will be displayed at the KRV 8th Annual European Medical Information and Communications Conference - See more at: http://www.krvportal.org/Meetings-and-Training/Find-Meetings-and-Training/Meeting-Details.aspx?ProductID=4718263&EventType=Meeting#sthash.qWm3Tx8b.kfoz.

Audience

Attendees of this conference are budget holders and decision makers. They can chose to outsource copy review to organisation like ours, however, many pharma companies currently keep this function is house and waste internal resource, time and money.

Objective

Our objective is demonstrate from our findings that massive savings can be found by getting copy right first time.

Design Guidelines

This poster should not be heavily branded - as this CANNOT be promotional however you may include our logo with the authors names. We would like you to use our brand guidelines, however, in order that it is clear that this study was conducted by ourselves. Brand book is attached plus our logos and icons.

Examples of academic posters can be found with a quick google search - one source that I have found useful is http://boristhalway.com/tips/academic/posterdesign I have attached an example of the kind of layout we would like to see... please keep the background quite plain as this will make it easier to read

Within the copy attached data graphs have been included for position guidance only and an excel file with the raw data and graphs is also attached - if you feel that the data can be displayed more effectively please do... also please apply our brand style. It is important that the data is accurately reproduced.

Attachments

An example of layout that we would like you to consider

Copy

```html
<!DOCTYPE html>
<html lang="en">
<head>
<meta charset="utf-8">
<title>Copy Review Resource Utilisation – Academic Poster</title>
<link href="https://fonts.googleapis.com/css2?family=Arimo:wght@400;700&display=swap" rel="stylesheet">
<style>
:root{
  --band-dark:#8593ad;
  --band-light:#d3d9e4;
  --pill-top:#b9c2d4;
  --pill-bottom:#7f8ea9;
  --ink:#3a3a3a;
  --muted:#8a8f99;
  --panel:#ffffff;
  --backdrop:#dedede;
  --aims:#e6e6e6;
  --blue:#6f9fd8;
  --red:#e05a55;
  --green:#b6d67a;
  --purple:#a993cf;
  --grid:#d0d0d0;
}
*{box-sizing:border-box;margin:0;padding:0}
html,body{width:1200px;height:994px;overflow:hidden;background:#fff}
body{font-family:"Arimo",Arial,sans-serif;color:var(--ink);position:relative}
.abs{position:absolute}
.header{left:0;top:0;width:1200px;height:160px;background:linear-gradient(180deg,var(--band-dark) 0%,#a6b1c5 60%,var(--band-light) 100%)}
.brand{display:flex;align-items:center;gap:10px;color:#fff;font-weight:700}
.brand .dot{width:34px;height:34px;border-radius:50%;background:#fff}
.header .brand{left:44px;top:52px;font-size:30px}
.title{left:232px;top:24px;width:950px;color:#fff;font-weight:700;font-size:19.5px;line-height:29px;text-transform:uppercase;text-shadow:1px 1px 2px rgba(0,0,0,.35);letter-spacing:.2px}
.authors{left:540px;top:97px;color:#eef1f6;font-size:13px;line-height:17px}
.backdrop{background:var(--backdrop);border-radius:14px}
.pill{height:33px;border-radius:17px;background:linear-gradient(180deg,var(--pill-top),var(--pill-bottom));color:#fff;font-weight:700;font-size:18px;text-align:center;line-height:33px;text-transform:uppercase;box-shadow:0 2px 3px rgba(0,0,0,.25)}
.panel{background:var(--panel);border-radius:10px;box-shadow:0 1px 4px rgba(0,0,0,.18);font-size:8px;line-height:10.5px}
.panel p{margin-bottom:8px}
.intro{padding:18px 10px}
.boxes{display:flex;gap:4px;margin-bottom:10px}
.box{background:var(--aims);padding:8px 7px;flex:1;font-size:7.2px;line-height:9.5px}
.box h4{font-size:8px;line-height:10px;margin-bottom:6px}
.box ul,.aims ul,.method ul,.conclusions ul,.right-text ul{list-style:none}
.box li::before,.aims li::before,.method li::before,.conclusions li::before{content:"• "}
.aims{background:var(--aims);padding:8px 10px;font-size:7.2px;line-height:9.5px;margin-bottom:10px}
.aims h4,.method h4{text-align:center;font-size:8px;margin-bottom:6px}
.center-bold{text-align:center;font-weight:700}
.method{padding:14px 10px}
.method .box-inner{background:var(--aims);padding:8px 10px;margin-bottom:12px;font-size:7.2px;line-height:9.5px}
.contact{left:30px;color:var(--muted)}
.contact b{color:#6b7fa3}
.card{background:#fff;border-radius:8px;font-size:7.6px;line-height:9.6px}
.card .lead{font-weight:700}
.chart-title{font-weight:700;font-size:11px;font-family:Georgia,"Times New Roman",serif;text-align:center}
svg text{font-family:"Arimo",Arial,sans-serif}
.conclusions{padding:16px 12px;font-size:7.8px;line-height:10px}
.conclusions .key{background:var(--aims);padding:8px 10px;font-size:8px;line-height:11px}
.conclusions .key h4{font-size:8.4px;margin-bottom:5px}
.right-text{font-size:8px;line-height:10.5px}
.right-text li::before{content:"• "}
.rank{background:#fff;border-radius:8px;padding:6px 8px}
.rank h4{text-align:center;font-size:8.5px;margin-bottom:6px}
.rank table{width:100%;border-collapse:collapse;font-size:7.5px}
.rank th{font-size:9.5px;text-align:center;padding:3px 0;border-bottom:1px solid #ccc}
.rank td{text-align:center;padding:5px 0;border-bottom:1px solid #e2e2e2}
.rank td.reason{text-align:right;padding-right:6px}
</style>
</head>
<body>

<div class="abs header"></div>
<div class="abs brand" style="left:44px;top:54px;font-size:30px"><span class="dot"></span>CodaVetta</div>
<h1 class="abs title">A survey of three pharmaceutical companies’ resource utilisation in<br>copy review activities and proposals for business process improvement</h1>
<div class="abs authors">Elena Marwick, director, CodaVetta Ltd, London<br>Hugo Tillbrook, director, CodaVetta Ltd, London</div>

<!-- backdrops -->
<div class="abs backdrop" style="left:344px;top:226px;width:520px;height:750px"></div>
<div class="abs backdrop" style="left:850px;top:604px;width:342px;height:372px"></div>

<!-- Introduction -->
<div class="abs pill" style="left:22px;top:183px;width:300px">Introduction</div>
<section class="abs panel intro" style="left:22px;top:212px;width:300px;height:330px">
  <p>Promotional and non-promotional materials are highly visible outputs of pharmaceutical companies. They are scrutinised by competitors, agencies and sometimes customers. Penalties for errors can be significant, measured in time, reputation or monetary fines.</p>
  <div class="boxes">
    <div class="box"><h4>Central to nearly all codes and systems are requirements that statements and messages are:</h4>
      <ul><li>Consistent with the marketing authorisation;</li><li>Accurate and capable of substantiation;</li><li>Fair, balanced and up to date.</li></ul></div>
    <div class="box"><h4>Regional and national differences exist in the regulation of:</h4>
      <ul><li>Meetings;</li><li>Gifts, fees, hospitality and travel;</li><li>External approval requirements;</li><li>Dispute resolution.</li></ul></div>
  </div>
  <p>The UK industry body, UKPMA, issued a code of conduct in 1958. Its current form is very similar to the European industry EPMF code. Many UK pharmaceutical companies place considerable importance on adherence to the code, with large teams working on the review of materials and activities.</p>
  <p>Copy review is a now a significant activity that consumes considerable resources, in the form of time, of some of the most expensive and scientifically able members of staff.</p>
  <div class="aims"><h4>The aims of this study were to</h4>
    <ul><li>quantify time taken up by copy review activities in a sample of UK pharmaceutical affiliates medical affairs and commercial functions;</li><li>identify the origins and consequences of avoidable re-work;</li><li>develop solutions.</li></ul></div>
  <p class="center-bold">We present here the medical affairs results.</p>
</section>

<!-- Method -->
<div class="abs pill" style="left:22px;top:617px;width:300px">Method</div>
<section class="abs panel method" style="left:22px;top:650px;width:300px;height:135px">
  <div class="box-inner"><h4>We developed an online survey with three components:</h4>
    <ul><li>Retrospective, quantitative estimates of time taken on copy review and numbers of avoidable iterations;</li><li>Ranking the common reasons for avoidable iterations;</li><li>Free text responses describing potential solutions.</li></ul></div>
  <p class="center-bold">This was sent to 249 staff in three UK pharmaceutical companies in 2013 and 2014.</p>
</section>

<div class="abs brand" style="left:120px;top:830px;font-size:22px;color:#6b7fa3"><span class="dot" style="width:26px;height:26px;background:#6b7fa3"></span>CodaVetta</div>
<div class="abs contact" style="top:905px;font-size:21px"><b>info@codavetta.co.uk</b></div>
<div class="abs contact" style="top:934px;font-size:19px">Phone <b>+44 (0) 208 555 0190</b></div>

<!-- Results -->
<div class="abs pill" style="left:342px;top:183px;width:514px">Results</div>

<section class="abs card" style="left:363px;top:238px;width:480px;height:152px;padding:10px 14px">
  <p class="lead">We received 118 usable responses from 249 invitations, a response rate of 47%. 48 responses were from medical affairs and 70 from commercial and other functions. The proportion of the working week spent on copy review by physicians was a consistent 40%. For medical information, the proportion varied between zero and 65%. Scientific advisors spent 0% to 42% of their time on copy activities.</p>
  <svg width="480" height="100" viewBox="0 0 480 100" style="position:absolute;left:0;top:52px">
    <g font-size="5.5" fill="#555">
      <!-- A 0-50 -->
      <g transform="translate(0,0)">
        <line x1="20" y1="10" x2="80" y2="10" stroke="var(--grid)" stroke-width=".5"/><line x1="20" y1="31" x2="80" y2="31" stroke="var(--grid)" stroke-width=".5"/><line x1="20" y1="52" x2="80" y2="52" stroke="var(--grid)" stroke-width=".5"/><line x1="20" y1="73" x2="80" y2="73" stroke="#999" stroke-width=".5"/>
        <text x="16" y="12" text-anchor="end">50</text><text x="16" y="33" text-anchor="end">30</text><text x="16" y="54" text-anchor="end">10</text><text x="16" y="75" text-anchor="end">0</text>
        <rect x="26" y="41" width="8" height="32" fill="var(--blue)"/><rect x="66" y="39" width="8" height="34" fill="var(--blue)"/>
        <text transform="translate(30,90) rotate(-45)">Med affs</text><text transform="translate(50,90) rotate(-45)">Med info</text><text transform="translate(70,90) rotate(-45)">SA/MSL</text>
        <rect x="86" y="43" width="4" height="4" fill="var(--blue)"/><text x="93" y="47">% of working</text><text x="93" y="54">week on copy</text><text x="93" y="61">Company A</text>
      </g>
      <g transform="translate(158,0)">
        <line x1="20" y1="10" x2="80" y2="10" stroke="var(--grid)" stroke-width=".5"/><line x1="20" y1="31" x2="80" y2="31" stroke="var(--grid)" stroke-width=".5"/><line x1="20" y1="52" x2="80" y2="52" stroke="var(--grid)" stroke-width=".5"/><line x1="20" y1="73" x2="80" y2="73" stroke="#999" stroke-width=".5"/>
        <text x="16" y="12" text-anchor="end">60</text><text x="16" y="33" text-anchor="end">40</text><text x="16" y="54" text-anchor="end">20</text><text x="16" y="75" text-anchor="end">0</text>
        <rect x="26" y="26" width="8" height="47" fill="var(--red)"/><rect x="46" y="23" width="8" height="50" fill="var(--red)"/><rect x="66" y="45" width="8" height="28" fill="var(--red)"/>
        <text transform="translate(30,90) rotate(-45)">Med affs</text><text transform="translate(50,90) rotate(-45)">Med info</text><text transform="translate(70,90) rotate(-45)">SA/MSL</text>
        <rect x="86" y="43" width="4" height="4" fill="var(--red)"/><text x="93" y="47">% of working</text><text x="93" y="54">week on copy</text><text x="93" y="61">Company B</text>
      </g>
      <g transform="translate(316,0)">
        <line x1="20" y1="10" x2="80" y2="10" stroke="var(--grid)" stroke-width=".5"/><line x1="20" y1="31" x2="80" y2="31" stroke="var(--grid)" stroke-width=".5"/><line x1="20" y1="52" x2="80" y2="52" stroke="var(--grid)" stroke-width=".5"/><line x1="20" y1="73" x2="80" y2="73" stroke="#999" stroke-width=".5"/>
        <text x="16" y="12" text-anchor="end">80</text><text x="16" y="33" text-anchor="end">40</text><text x="16" y="54" text-anchor="end">20</text><text x="16" y="75" text-anchor="end">0</text>
        <rect x="26" y="49" width="8" height="24" fill="var(--green)"/><rect x="46" y="39" width="8" height="34" fill="var(--green)"/>
        <text transform="translate(30,90) rotate(-45)">Med affs</text><text transform="translate(50,90) rotate(-45)">Med info</text><text transform="translate(70,90) rotate(-45)">SA/MSL</text>
        <rect x="86" y="43" width="4" height="4" fill="var(--green)"/><text x="93" y="47">% of working</text><text x="93" y="54">week on copy</text><text x="93" y="61">Company C</text>
      </g>
    </g>
  </svg>
</section>

<section class="abs card" style="left:363px;top:403px;width:228px;height:204px;padding:10px 14px">
  <p class="lead">On average just over 50% of time spent on copy activities went on checking scientific statements and claims. The remainder was spent on concept and planning meetings, commissioning, proof reading, compiling materials. Rounds of scheduled review averaged 2.3.</p>
  <div class="chart-title" style="margin-top:8px">% of copy time x activity, all MA %</div>
  <svg width="200" height="90" viewBox="0 0 200 90" style="margin-top:2px">
    <g transform="translate(50,45)">
      <path d="M0 0 L0 -40 A40 40 0 1 1 -4 39.8 Z" fill="var(--blue)"/>
      <path d="M0 0 L-4 39.8 A40 40 0 0 1 -36 -17.4 Z" fill="var(--red)"/>
      <path d="M0 0 L-36 -17.4 A40 40 0 0 1 -22 -33.4 Z" fill="var(--green)"/>
      <path d="M0 0 L-22 -33.4 A40 40 0 0 1 0 -40 Z" fill="var(--purple)"/>
    </g>
    <g font-size="5.5" fill="#444">
      <rect x="108" y="28" width="4" height="4" fill="var(--blue)"/><text x="115" y="32">Statements and claims</text>
      <rect x="108" y="40" width="4" height="4" fill="var(--red)"/><text x="115" y="44">Meetings</text>
      <rect x="108" y="52" width="4" height="4" fill="var(--green)"/><text x="115" y="56">Compiling</text>
      <rect x="108" y="64" width="4" height="4" fill="var(--purple)"/><text x="115" y="68">Commissioning</text>
    </g>
  </svg>
</section>

<section class="abs card" style="left:607px;top:403px;width:236px;height:204px;padding:14px 12px">
  <p class="lead">Estimates of the proportion of jobs requiring avoidable rounds of review ranged between 30 and 50%.</p>
  <div class="chart-title" style="margin-top:34px">% jobs needing extra rounds %</div>
  <svg width="200" height="60" viewBox="0 0 200 60" style="margin-top:4px">
    <g font-size="5.5" fill="#555">
      <line x1="20" y1="8" x2="80" y2="8" stroke="var(--grid)" stroke-width=".5"/><line x1="20" y1="24" x2="80" y2="24" stroke="var(--grid)" stroke-width=".5"/><line x1="20" y1="40" x2="80" y2="40" stroke="#999" stroke-width=".5"/>
      <text x="16" y="10" text-anchor="end">100</text><text x="16" y="26" text-anchor="end">50</text><text x="16" y="42" text-anchor="end">0</text>
      <rect x="26" y="26" width="8" height="14" fill="var(--blue)"/><rect x="46" y="26" width="8" height="14" fill="var(--blue)"/><rect x="66" y="29" width="8" height="11" fill="var(--blue)"/>
      <text x="30" y="50" text-anchor="middle">A</text><text x="50" y="50" text-anchor="middle">B</text><text x="70" y="50" text-anchor="middle">C</text>
      <rect x="86" y="18" width="4" height="4" fill="var(--blue)"/><text x="93" y="22">% jobs</text><text x="93" y="29">needing</text><text x="93" y="36">extra rounds</text><text x="93" y="43">%</text>
    </g>
  </svg>
</section>

<section class="abs card" style="left:363px;top:626px;width:480px;height:143px;padding:10px 14px">
  <p class="lead" style="text-align:center">This results in between six and eight additional hours work per week...</p>
  <svg width="480" height="110" viewBox="0 0 480 110" style="position:absolute;left:0;top:30px">
    <g font-size="5.5" fill="#555">
      <g transform="translate(10,0)">
        <text x="58" y="14" font-size="11" font-weight="700" font-family="Georgia,serif" text-anchor="middle">Phys</text>
        <line x1="20" y1="24" x2="100" y2="24" stroke="var(--grid)" stroke-width=".5"/><line x1="20" y1="37" x2="100" y2="37" stroke="var(--grid)" stroke-width=".5"/><line x1="20" y1="50" x2="100" y2="50" stroke="#999" stroke-width=".5"/>
        <text x="16" y="26" text-anchor="end">10</text><text x="16" y="39" text-anchor="end">5</text><text x="16" y="52" text-anchor="end">0</text>
        <rect x="30" y="34" width="10" height="16" fill="var(--blue)"/><rect x="55" y="31" width="10" height="19" fill="var(--blue)"/><rect x="80" y="37" width="10" height="13" fill="var(--blue)"/>
        <text x="35" y="60" text-anchor="middle">A</text><text x="60" y="60" text-anchor="middle">B</text><text x="85" y="60" text-anchor="middle">C</text><text x="60" y="70" text-anchor="middle">Company</text>
        <rect x="106" y="35" width="4" height="4" fill="var(--blue)"/><text x="113" y="39">Phys</text>
      </g>
      <g transform="translate(160,0)">
        <text x="58" y="14" font-size="11" font-weight="700" font-family="Georgia,serif" text-anchor="middle">SA/MSL</text>
        <line x1="20" y1="24" x2="100" y2="24" stroke="var(--grid)" stroke-width=".5"/><line x1="20" y1="37" x2="100" y2="37" stroke="var(--grid)" stroke-width=".5"/><line x1="20" y1="50" x2="100" y2="50" stroke="#999" stroke-width=".5"/>
        <text x="16" y="26" text-anchor="end">10</text><text x="16" y="39" text-anchor="end">5</text><text x="16" y="52" text-anchor="end">0</text>
        <rect x="30" y="29" width="10" height="21" fill="var(--green)"/><rect x="55" y="29" width="10" height="21" fill="var(--green)"/>
        <text x="35" y="60" text-anchor="middle">A</text><text x="60" y="60" text-anchor="middle">B</text><text x="85" y="60" text-anchor="middle">C</text><text x="60" y="70" text-anchor="middle">Company</text>
        <rect x="106" y="35" width="4" height="4" fill="var(--green)"/><text x="113" y="39">SA/MSL</text>
      </g>
      <g transform="translate(315,0)">
        <text x="58" y="14" font-size="11" font-weight="700" font-family="Georgia,serif" text-anchor="middle">Med info</text>
        <line x1="20" y1="20" x2="100" y2="20" stroke="var(--grid)" stroke-width=".5"/><line x1="20" y1="30" x2="100" y2="30" stroke="var(--grid)" stroke-width=".5"/><line x1="20" y1="40" x2="100" y2="40" stroke="var(--grid)" stroke-width=".5"/><line x1="20" y1="50" x2="100" y2="50" stroke="#999" stroke-width=".5"/>
        <text x="16" y="22" text-anchor="end">20</text><text x="16" y="32" text-anchor="end">15</text><text x="16" y="42" text-anchor="end">5</text><text x="16" y="52" text-anchor="end">0</text>
        <rect x="55" y="29" width="10" height="21" fill="var(--red)"/><rect x="80" y="24" width="10" height="26" fill="var(--red)"/>
        <text x="35" y="60" text-anchor="middle">A</text><text x="60" y="60" text-anchor="middle">B</text><text x="85" y="60" text-anchor="middle">C</text><text x="60" y="70" text-anchor="middle">Company</text>
        <rect x="106" y="35" width="4" height="4" fill="var(--red)"/><text x="113" y="39">Med info</text>
      </g>
    </g>
  </svg>
</section>

<section class="abs card" style="left:363px;top:786px;width:228px;height:166px;padding:14px 14px">
  <p class="lead">... and raised levels of friction, reported as ‘frequent’ or ‘common’ by 80% in one organization and to a significant level in all three.</p>
  <div class="chart-title" style="margin-top:12px">Friction</div>
  <svg width="200" height="70" viewBox="0 0 200 70" style="margin-top:2px">
    <g font-size="5.5" fill="#555">
      <line x1="20" y1="8" x2="90" y2="8" stroke="var(--grid)" stroke-width=".5"/><line x1="20" y1="26" x2="90" y2="26" stroke="var(--grid)" stroke-width=".5"/><line x1="20" y1="44" x2="90" y2="44" stroke="#999" stroke-width=".5"/>
      <text x="16" y="10" text-anchor="end">100</text><text x="16" y="28" text-anchor="end">50</text><text x="16" y="46" text-anchor="end">0</text>
      <rect x="28" y="19" width="9" height="25" fill="var(--blue)"/><rect x="51" y="15" width="9" height="29" fill="var(--blue)"/><rect x="74" y="17" width="9" height="27" fill="var(--blue)"/>
      <text x="32" y="54" text-anchor="middle">A</text><text x="55" y="54" text-anchor="middle">B</text><text x="78" y="54" text-anchor="middle">C</text>
      <rect x="96" y="24" width="4" height="4" fill="var(--blue)"/><text x="103" y="28">Friction</text>
    </g>
  </svg>
</section>

<section class="abs card" style="left:607px;top:786px;width:236px;height:166px;padding:14px 14px">
  <p class="lead">Missed deadlines were estimated for around one third of projects.</p>
  <div class="chart-title" style="margin-top:22px">Missed deadlines</div>
  <svg width="200" height="80" viewBox="0 0 200 80" style="margin-top:2px">
    <g font-size="5.5" fill="#555">
      <line x1="20" y1="6" x2="90" y2="6" stroke="var(--grid)" stroke-width=".5"/><line x1="20" y1="17" x2="90" y2="17" stroke="var(--grid)" stroke-width=".5"/><line x1="20" y1="28" x2="90" y2="28" stroke="var(--grid)" stroke-width=".5"/><line x1="20" y1="39" x2="90" y2="39" stroke="var(--grid)" stroke-width=".5"/><line x1="20" y1="50" x2="90" y2="50" stroke="var(--grid)" stroke-width=".5"/><line x1="20" y1="61" x2="90" y2="61" stroke="#999" stroke-width=".5"/>
      <text x="16" y="8" text-anchor="end">50</text><text x="16" y="19" text-anchor="end">40</text><text x="16" y="30" text-anchor="end">30</text><text x="16" y="41" text-anchor="end">20</text><text x="16" y="52" text-anchor="end">10</text><text x="16" y="63" text-anchor="end">0</text>
      <rect x="28" y="31" width="9" height="30" fill="var(--green)"/><rect x="51" y="15" width="9" height="46" fill="var(--green)"/><rect x="74" y="20" width="9" height="41" fill="var(--green)"/>
      <text x="32" y="71" text-anchor="middle">A</text><text x="55" y="71" text-anchor="middle">B</text><text x="78" y="71" text-anchor="middle">C</text>
      <rect x="96" y="30" width="4" height="4" fill="var(--green)"/><text x="103" y="34">Missed</text><text x="103" y="41">deadlines</text>
    </g>
  </svg>
</section>

<!-- Conclusions -->
<div class="abs pill" style="left:880px;top:183px;width:298px">Conclusions</div>
<section class="abs panel conclusions" style="left:880px;top:212px;width:298px;height:370px">
  <p>Between one third and one half of the available resource in medical affairs teams in the UK is taken up reviewing materials. This varies between organisations depending upon allocation of this activity. Materials are seen multiple times and a significant proportion of iterations are seen again and again. This causes loss of productivity and internal friction between and within departments. Scientists and physicians engaged in review have positive proposals for process improvement, which are consistent across the organisations involved in this piece of work.</p>
  <p>This small survey identifies potential best practice. The interventions proposed are not proven to reduce waste in the copy review process. However, it seems likely that pharmaceutical companies could save time and money by adopting some simple solutions aimed at ensuring only good quality, scientifically valid material enters the review cycle, and by defining review standards, roles and responsibilities. Physicians and scientists could be released from desk work to undertake customer facing activities or conduct studies. Hard to fill posts and subsequent reliance on contractors could be reduced.</p>
  <p>This activity has crept up on the industry, to the point now that reviewing copy has become an industry within an industry, occupying half of the working lives of hundreds of medical information specialists and pharmaceutical physicians in the UK. This is not mission critical work and is a diversion from the productive and real work of supporting patients and helping customers to understand medicines.</p>
  <p>An industry-wide prospective survey is necessary to identify actual resource utilisation in this activity and benchmark best vs worst practice. Process improvement interventions could be formally assessed to measure the savings that can be made.</p>
  <div class="key"><h4>It is likely that three relatively simple actions could save a lot of time:</h4>
    <ul><li>Improve the standards of materials entering the review cycle;</li><li>Define and limit responsibilities.</li></ul></div>
</section>

<div class="abs right-text" style="left:857px;top:620px;width:320px">
  <p>The three top-ranked reasons for re-work were:</p>
  <ul><li>claims not supported;</li><li>references missing or not marked up;</li><li>differences of opinion.</li></ul>
</div>

<div class="abs rank" style="left:857px;top:673px;width:272px;height:180px">
  <h4>Ranked reasons for re-work</h4>
  <table>
    <thead><tr><th>A</th><th>B</th><th>C</th><th></th></tr></thead>
    <tbody>
      <tr><td>1</td><td>1</td><td>2</td><td class="reason">Claims not supportable</td></tr>
      <tr><td>2</td><td>2</td><td>1</td><td class="reason">References missing or not marked</td></tr>
      <tr><td>3</td><td>4</td><td>4</td><td class="reason">Difference in opinion in interpreting the Code</td></tr>
      <tr><td>6</td><td>3</td><td>3</td><td class="reason">Spelling and grammar</td></tr>
      <tr><td>4</td><td>5</td><td>5</td><td class="reason">Other technical Code issue</td></tr>
      <tr><td>5</td><td>7</td><td>6</td><td class="reason">Review criteria changed during project</td></tr>
      <tr><td>7</td><td>6</td><td>7</td><td class="reason">Layout or presentation</td></tr>
    </tbody>
  </table>
</div>

<div class="abs right-text" style="left:857px;top:897px;width:325px">
  <p>Free text proposed solutions from respondents were grouped subjectively into themes. The three most frequent cited proposals were:</p>
  <ul><li>meetings to discuss materials before copy got into the review cycle;</li><li>improve the scientific accuracy and spelling of copy before review, so that it is right first time;</li><li>insist on consistency between reviewers and between reviews cycles.</li></ul>
</div>

</body>
</html>
```